Interior Design/ decoration business card design

This card is for my Interior Design and Decoration business and later I will also be selling homewares. I would like the card to be very simple in design and like either white, duck egg blue , aquas or metallics on a flat mat card excellent quality card. It needs to be well designed as that is my field. I dont like fuss, the simpler the better. I would like a styalised wren under the name wren if possible. SIMPLE, STYLISH, CLASSIC, TASTEFUL

Target Market(s)

40 + year olds who are building or rennovating.

Industry/Entity Type

Business

Contact Information for Business Card

Wren
styling, design, homeware

Maren Tulloch
p 0437165093
e maren@wrenliving.com.au
w wrenliving.com.au

Requirements
Must have
• very simple, stylish, classic, sophisticated. Simple and easy to read text that is a print similar to attached image. I like simple round A's though not as in attached image.

Double sided. It wont save as double sided for some reason!!
Should not have
• not too much colour, No animated / cartoon pictures.

```html
<!DOCTYPE html>
<html lang="en">
<head>
<meta charset="utf-8">
<title>Wren – Business Card</title>
<link href="https://fonts.googleapis.com/css2?family=Questrial&family=Montserrat:wght@600&display=swap" rel="stylesheet">
<style>
  :root {
    --page: #e9e7e4;
    --card: #ffffff;
    --aqua: #a8d2ce;
    --ink: #3f3531;
    --text: #4d4d4d;
    --shadow: rgba(40, 30, 25, 0.18);
  }
  * { box-sizing: border-box; margin: 0; padding: 0; }
  html, body {
    width: 1200px;
    height: 577px;
    overflow: hidden;
    background: var(--page);
    font-family: "Questrial", sans-serif;
    color: var(--text);
  }
  .sheet {
    position: relative;
    width: 1200px;
    height: 577px;
  }
  .card {
    position: absolute;
    top: 128px;
    width: 520px;
    height: 310px;
    background: var(--card);
    box-shadow: 0 6px 18px var(--shadow);
  }
  .card--contact { left: 50px; }
  .card--brand { left: 630px; }

  /* Brand name block */
  .brand {
    display: flex;
    flex-direction: column;
    align-items: center;
    text-align: center;
  }
  .brand__name {
    font-family: "Questrial", sans-serif;
    color: var(--ink);
    text-transform: uppercase;
    letter-spacing: 0.3em;
    line-height: 1;
    padding-left: 0.3em;
  }
  .brand__services {
    font-family: "Questrial", sans-serif;
    color: var(--text);
    letter-spacing: 0.08em;
    white-space: nowrap;
  }

  /* Contact side */
  .card--contact .brand {
    position: absolute;
    left: 20px;
    top: 136px;
    width: 220px;
  }
  .card--contact .brand__name { font-size: 30px; margin-bottom: 20px; }
  .card--contact .brand__services { font-size: 13px; }

  .identity {
    position: absolute;
    right: 40px;
    top: 34px;
    text-align: right;
  }
  .identity__name {
    font-family: "Montserrat", sans-serif;
    font-weight: 600;
    font-size: 14px;
    color: var(--aqua);
    letter-spacing: 0.01em;
  }
  .identity__role {
    font-size: 12.5px;
    color: var(--text);
    margin-top: 1px;
  }

  .rule {
    position: absolute;
    left: 268px;
    top: 112px;
    width: 3px;
    height: 112px;
    background: var(--aqua);
  }

  .contacts {
    position: absolute;
    left: 296px;
    top: 124px;
    list-style: none;
  }
  .contacts__item {
    display: flex;
    align-items: center;
    gap: 9px;
    font-size: 12.5px;
    color: var(--ink);
    margin-bottom: 11px;
  }
  .contacts__icon {
    width: 15px;
    height: 15px;
    background: var(--aqua);
    display: flex;
    align-items: center;
    justify-content: center;
    flex: none;
  }

  /* Brand side */
  .card--brand .brand {
    position: absolute;
    left: 0;
    right: 0;
    top: 112px;
  }
  .card--brand .brand__name { font-size: 40px; margin-bottom: 26px; }
  .card--brand .brand__services { font-size: 16px; }
</style>
</head>
<body>
<main class="sheet">

  <section class="card card--contact" aria-label="Business card, contact side">
    <div class="identity">
      <p class="identity__name">Maren Tulloch</p>
      <p class="identity__role">Homeware Expert</p>
    </div>

    <div class="brand">
      <p class="brand__name">Wren</p>
      <p class="brand__services">styling · design · homeware</p>
    </div>

    <div class="rule"></div>

    <ul class="contacts">
      <li class="contacts__item">
        <span class="contacts__icon">
          <svg width="9" height="11" viewBox="0 0 9 11" aria-hidden="true">
            <rect x="1" y="0.5" width="7" height="10" rx="1.2" fill="none" stroke="#fff" stroke-width="1.2"/>
            <line x1="3.5" y1="8.6" x2="5.5" y2="8.6" stroke="#fff" stroke-width="1"/>
          </svg>
        </span>
        0437 165 093
      </li>
      <li class="contacts__item">
        <span class="contacts__icon">
          <svg width="11" height="8" viewBox="0 0 11 8" aria-hidden="true">
            <rect x="0.6" y="0.6" width="9.8" height="6.8" fill="none" stroke="#fff" stroke-width="1.1"/>
            <polyline points="0.8,0.9 5.5,4.6 10.2,0.9" fill="none" stroke="#fff" stroke-width="1.1"/>
          </svg>
        </span>
        maren@wrenliving.com.au
      </li>
      <li class="contacts__item">
        <span class="contacts__icon">
          <svg width="11" height="11" viewBox="0 0 11 11" aria-hidden="true">
            <circle cx="5.5" cy="5.5" r="4.6" fill="none" stroke="#fff" stroke-width="1.1"/>
            <polyline points="5.5,2.8 5.5,5.5 7.6,6.8" fill="none" stroke="#fff" stroke-width="1.1"/>
          </svg>
        </span>
        wrenliving.com.au
      </li>
    </ul>
  </section>

  <section class="card card--brand" aria-label="Business card, brand side">
    <div class="brand">
      <p class="brand__name">Wren</p>
      <p class="brand__services">styling · design · homeware</p>
    </div>
  </section>

</main>
</body>
</html>
```